A combined poster for Martial arts club and Dance club.

We need a poster that will be hung opp and used in street bucks for advertisement. We are two independent clubs ( a dance studio and a MA gym) but have chosen to cooperate and split costs for advertisement. We also see an effect with both arts on the same poster.

We have a attached a picture with both arts doing a pose from each other. This would be great to use.

Target Market(s)

All ages primarily young people

Industry/Entity Type

Martial Art

Colors

Designer to choose colors to be used in the design.

Requirements
Must have
• A professional look. Both logos and either one of the attached pictures.
• Fight styles: Check webpage: http://www.kestrelforge.no
• Dance Styles: http://tramvikdansehus4.com
• Contact information Address and phone
• Space for texts slogans.
Nice to have
• Photoshop the picture with different background or cut them out.

```html
<!DOCTYPE html>
<html lang="no">
<head>
<meta charset="utf-8">
<title>Kestrel Forge Academy &amp; Tramvik Dansehus 4</title>
<link rel="stylesheet" href="https://fonts.googleapis.com/css2?family=Oswald:wght@700&family=Roboto:wght@900&display=swap">
<style>
  :root {
    --wall-dark: #233032;
    --wall-mid: #4d5a5c;
    --floor-light: #e6e8e8;
    --floor-pale: #f2f2f2;
    --gi-light: #dfe2e3;
    --gi-shadow: #aeb3b6;
    --tutu-blue: #5c6a82;
    --tutu-pale: #d9d6d0;
    --accent-blue: #3d8fd6;
    --accent-red: #e01b1b;
    --text-light: #ffffff;
    --text-dark: #111111;
  }
  * { margin: 0; padding: 0; box-sizing: border-box; }
  html, body { width: 849px; height: 1200px; overflow: hidden; background: var(--floor-pale); }
  .poster {
    position: relative;
    width: 849px;
    height: 1200px;
    overflow: hidden;
    font-family: "Oswald", "Arial Narrow", sans-serif;
    font-weight: 700;
  }
  .backdrop {
    position: absolute; inset: 0;
    background: linear-gradient(180deg, var(--wall-dark) 0%, #2f3c3e 35%, var(--wall-mid) 52%, #b9bebe 63%, var(--floor-light) 72%, var(--floor-pale) 100%);
  }
  .photo {
    position: absolute;
    border-radius: 18px;
  }
  .photo--fighter {
    left: 452px; top: 85px; width: 378px; height: 535px;
    background: linear-gradient(160deg, var(--gi-light) 0%, var(--gi-shadow) 100%);
  }
  .photo--dancer {
    left: 95px; top: 375px; width: 295px; height: 570px;
    background: linear-gradient(180deg, var(--tutu-pale) 0%, var(--tutu-blue) 35%, var(--tutu-pale) 60%, #cdbfb8 100%);
  }
  .style-list {
    position: absolute;
    text-transform: uppercase;
    font-size: 30px;
    line-height: 34.5px;
    letter-spacing: 0;
  }
  .style-list h2 { font-size: 38px; line-height: 44px; font-weight: 700; }
  .style-list li { list-style: none; }
  .style-list--martial { left: 53px; top: 62px; color: var(--text-light); }
  .style-list--martial h2 { color: var(--accent-blue); }
  .style-list--dance { left: 471px; top: 728px; color: var(--text-dark); }
  .style-list--dance h2 { color: var(--accent-red); }
  .rule { position: absolute; height: 5px; }
  .rule--blue { left: 0; top: 329px; width: 364px; background: var(--accent-blue); }
  .rule--red { left: 470px; top: 692px; width: 379px; background: var(--accent-red); }
  .club-name {
    position: absolute;
    display: flex; align-items: center; gap: 10px;
    font-size: 34px; line-height: 1; text-transform: uppercase;
  }
  .club-name--martial { left: 620px; top: 40px; width: 180px; flex-direction: column; gap: 8px; color: var(--text-light); text-align: center; }
  .club-name--martial .mark { width: 120px; height: 120px; border-radius: 50%; background: var(--accent-blue); }
  .club-name--dance { left: 78px; top: 1005px; color: var(--text-dark); }
  .club-name--dance .mark { width: 30px; height: 30px; background: var(--accent-red); }
  .address {
    position: absolute; left: 0; right: 0; top: 1112px;
    text-align: center;
    font-family: "Roboto", Arial, sans-serif;
    font-weight: 900; font-size: 40px; line-height: 48px; color: var(--text-dark);
    letter-spacing: 2px;
  }
</style>
</head>
<body>
<main class="poster">
  <div class="backdrop" role="img" aria-label="Dark weathered concrete wall fading into a pale studio floor"></div>
  <div class="photo photo--fighter" role="img" aria-label="Martial artist in a white gi and black belt leaping in a ballet pose"></div>
  <div class="photo photo--dancer" role="img" aria-label="Ballerina in a blue tutu standing in a boxing guard"></div>

  <section class="style-list style-list--martial">
    <h2>Kampsport</h2>
    <ul>
      <li>Brasiliansk jiu jitsu</li>
      <li>Mixed martial arts</li>
      <li>Thaiboksing</li>
      <li>Submission wrestling</li>
      <li>Kyokushin karate</li>
      <li>Barn og ungdom</li>
    </ul>
  </section>
  <div class="rule rule--blue"></div>

  <div class="club-name club-name--martial"><span class="mark"></span>Kestrel Forge</div>

  <div class="rule rule--red"></div>
  <section class="style-list style-list--dance">
    <h2>Dans</h2>
    <ul>
      <li>Jazz freestyle</li>
      <li>Disco cheerdance</li>
      <li>Basistrening</li>
      <li>Akrobatikk / turn</li>
      <li>Slow dance</li>
      <li>Barn m/spesielle behov</li>
    </ul>
  </section>

  <div class="club-name club-name--dance"><span class="mark"></span>Tramvik Dansehus 4</div>

  <p class="address">Granliveien 38</p>
</main>
</body>
</html>
```